Korvane Works Business cards

We require somebody to design business cards for our new business.

Target Market(s)

Mining, haulage and civil.

Industry/Entity Type

Auto electrician in mining industry

Contact Information for Business Card

ABN, business email address, mobile number.

Colors
00AB8E
00BBA5
67D7C9
C6EFE9
E9F9F6

Requirements
Must have
• Services I offer: Breakdowns, Field Service, A/C Systems, Machine rewires, mine site vehicle fit outs

```html
<!DOCTYPE html>
<html lang="en">
<head>
<meta charset="utf-8">
<title>Korvane Works Business Cards</title>
<link rel="stylesheet" href="https://fonts.googleapis.com/css2?family=Roboto:wght@400;500;700&display=swap">
<style>
  :root {
    --teal-deep: #00AB8E;
    --teal: #00BBA5;
    --teal-light: #67D7C9;
    --teal-pale: #C6EFE9;
    --card: #000000;
    --backdrop: #3a3a3a;
    --ink: #ffffff;
  }
  * { margin: 0; padding: 0; box-sizing: border-box; }
  html, body {
    width: 1200px; height: 694px; overflow: hidden;
    background: var(--backdrop);
    font-family: "Roboto", Arial, sans-serif;
  }
  .stage { position: relative; width: 1200px; height: 694px; }
  .card {
    position: absolute; top: 192px;
    width: 540px; height: 310px;
    background: var(--card);
    border-radius: 22px;
    overflow: hidden;
    color: var(--ink);
  }
  .card--services { left: 40px; }
  .card--contact { left: 620px; }

  .brand {
    position: absolute;
    display: flex; align-items: center; gap: 10px;
    color: var(--teal-light);
    font-weight: 700; font-size: 26px; letter-spacing: 0.5px;
  }
  .brand__mark { width: 14px; height: 14px; background: var(--teal-light); }
  .card--services .brand { left: 34px; top: 138px; }
  .card--contact .brand { left: 36px; top: 92px; }

  .divider {
    position: absolute; left: 248px; top: 58px;
    width: 2px; height: 194px; background: var(--teal-deep);
  }
  .services { position: absolute; left: 278px; top: 62px; }
  .services__title {
    color: var(--teal); font-weight: 700; font-size: 22px;
    letter-spacing: 0.3px; margin-bottom: 6px;
  }
  .services__list { list-style: none; }
  .services__item { font-size: 19px; line-height: 31px; font-weight: 500; }
  .services__item::before { content: "•"; color: var(--teal); margin-right: 8px; }

  .identity { position: absolute; right: 40px; top: 42px; text-align: right; }
  .identity__name { color: var(--teal); font-weight: 700; font-size: 30px; }
  .identity__role { font-size: 18px; margin-top: 2px; }
  .accent-tab {
    position: absolute; right: 0; top: 36px;
    width: 14px; height: 56px; background: var(--teal-deep);
  }
  .rule { position: absolute; height: 1px; background: var(--ink); }
  .rule--top { left: 270px; right: 40px; top: 140px; }
  .rule--bottom { left: 36px; width: 200px; top: 212px; }

  .address {
    position: absolute; right: 40px; top: 152px;
    text-align: right; font-size: 17px; line-height: 25px;
  }
  .address__abn { color: var(--teal); font-weight: 700; }

  .contacts { position: absolute; left: 36px; top: 220px; list-style: none; }
  .contacts__item {
    display: flex; align-items: center; gap: 10px;
    font-size: 17px; line-height: 25px;
  }
  .contacts__icon { width: 16px; height: 16px; flex: none; }

  .base-band {
    position: absolute; left: 0; right: 0; bottom: 0;
    height: 9px; background: var(--teal-deep);
  }
</style>
</head>
<body>
<main class="stage">
  <section class="card card--services" aria-label="Services side">
    <div class="brand"><span class="brand__mark"></span>Korvane Works</div>
    <div class="divider"></div>
    <div class="services">
      <h2 class="services__title">SERVICES OFFER</h2>
      <ul class="services__list">
        <li class="services__item">Breakdowns</li>
        <li class="services__item">Field Service</li>
        <li class="services__item">A/C Systems</li>
        <li class="services__item">Machine rewires</li>
        <li class="services__item">Mine site vehicle fit outs</li>
      </ul>
    </div>
  </section>

  <section class="card card--contact" aria-label="Contact side">
    <div class="brand"><span class="brand__mark"></span>Korvane Works</div>
    <div class="accent-tab"></div>
    <div class="identity">
      <h1 class="identity__name">Ellis Varro</h1>
      <p class="identity__role">Owner</p>
    </div>
    <div class="rule rule--top"></div>
    <div class="address">
      <p>88, Quarry Road, Pit Lane</p>
      <p>40718, Australia</p>
      <p class="address__abn">ABN No. 908-317</p>
    </div>
    <div class="rule rule--bottom"></div>
    <ul class="contacts">
      <li class="contacts__item">
        <svg class="contacts__icon" viewBox="0 0 16 16" aria-hidden="true"><rect x="4" y="1" width="8" height="14" rx="1.5" fill="none" stroke="#00BBA5" stroke-width="1.6"/><circle cx="8" cy="12.5" r="0.9" fill="#00BBA5"/></svg>
        555.014.2087
      </li>
      <li class="contacts__item">
        <svg class="contacts__icon" viewBox="0 0 16 16" aria-hidden="true"><rect x="1" y="3" width="14" height="10" fill="#00BBA5"/><path d="M1 3 L8 9 L15 3" fill="none" stroke="#000" stroke-width="1.4"/></svg>
        info@korvaneworks.com
      </li>
      <li class="contacts__item">
        <svg class="contacts__icon" viewBox="0 0 16 16" aria-hidden="true"><circle cx="8" cy="8" r="7" fill="none" stroke="#00BBA5" stroke-width="1.6"/><ellipse cx="8" cy="8" rx="3" ry="7" fill="none" stroke="#00BBA5" stroke-width="1.2"/><line x1="1" y1="8" x2="15" y2="8" stroke="#00BBA5" stroke-width="1.2"/></svg>
        www.korvaneworks.com
      </li>
    </ul>
    <div class="base-band"></div>
  </section>
</main>
</body>
</html>
```